Lumora Activewear business card design

I need a business card designed for my activewear business. I would like to use the colours pink, purple white and blue. please see attached logo. please include (name) Harriet Welloby (phone) 0417582064 (email) hattieslumora@mailvento.com (ABN) 48715290637 . please include - Free shipping on all orders over $100

Target Market(s)

female

Contact Information for Business Card

Colors

Requirements
Must have
• I need a business card designed for my activewear business. I would like to use the colours pink, purple white and blue. please see attached logo. please include (name) Harriet Welloby (phone) 0417582064 (email) hattieslumora@mailvento.com (ABN) 48715290637 . please include - Free shipping on all orders over $100

```html
<!DOCTYPE html>
<html lang="en">
<head>
<meta charset="utf-8">
<title>Lumora Activewear – Business Card</title>
<link rel="stylesheet" href="https://fonts.googleapis.com/css2?family=Bebas+Neue&family=Open+Sans:ital,wght@0,400;0,600;1,700&display=swap">
<style>
  :root {
    --page-bg: #e4e4e6;
    --pink-soft: #f9dbe4;
    --pink-mid: #f4bccb;
    --pink-deep: #ef9fb4;
    --purple: #923a96;
    --purple-text: #9a3c9b;
    --mauve: #c87ba8;
    --magenta: #c2278f;
    --ink: #3d3540;
    --white: #ffffff;
  }
  * { box-sizing: border-box; margin: 0; padding: 0; }
  html, body { width: 1200px; height: 1200px; overflow: hidden; }
  body {
    background: var(--page-bg);
    position: relative;
    font-family: "Open Sans", Arial, sans-serif;
  }
  .card {
    position: absolute;
    left: 180px;
    width: 838px;
    height: 474px;
    overflow: hidden;
  }
  .card--front { top: 120px; }
  .card--back { top: 638px; }

  .card__backdrop {
    position: absolute;
    inset: 0;
    background:
      radial-gradient(circle at 30% 25%, rgba(255,255,255,.55) 0 8%, transparent 22%),
      radial-gradient(circle at 78% 30%, rgba(255,255,255,.5) 0 6%, transparent 20%),
      radial-gradient(circle at 45% 85%, rgba(255,255,255,.45) 0 6%, transparent 18%),
      radial-gradient(circle at 88% 80%, rgba(255,255,255,.35) 0 5%, transparent 16%),
      radial-gradient(ellipse at 50% 50%, var(--pink-soft) 0%, var(--pink-mid) 70%, var(--pink-deep) 100%);
  }

  .brand-name {
    position: absolute;
    font-family: "Open Sans", Arial, sans-serif;
    font-weight: 600;
    color: var(--purple-text);
    text-transform: uppercase;
    line-height: 1;
    white-space: nowrap;
  }

  /* Front */
  .front__name {
    left: 348px;
    top: 191px;
    font-size: 66px;
    letter-spacing: 9px;
  }
  .front__tagline {
    position: absolute;
    left: 398px;
    top: 262px;
    font-family: "Bebas Neue", Impact, sans-serif;
    color: var(--white);
    font-size: 54px;
    letter-spacing: 1px;
    line-height: 1;
  }

  /* Back */
  .back__band {
    position: absolute;
    inset: 0;
  }
  .back__band svg { width: 100%; height: 100%; display: block; }
  .back__name-brand {
    left: 178px;
    top: 73px;
    font-size: 45px;
    letter-spacing: 4px;
  }
  .back__rule {
    position: absolute;
    left: 204px;
    top: 126px;
    width: 148px;
    height: 3px;
    background: var(--purple);
    border-radius: 2px;
  }
  .back__person {
    position: absolute;
    left: 62px;
    top: 200px;
    font-family: "Bebas Neue", Impact, sans-serif;
    font-weight: 400;
    font-size: 54px;
    color: var(--purple-text);
    letter-spacing: .5px;
    line-height: 1;
  }
  .contact-list {
    position: absolute;
    left: 62px;
    top: 258px;
    list-style: none;
  }
  .contact-list li {
    display: flex;
    align-items: center;
    height: 36px;
    font-size: 23px;
    color: var(--ink);
  }
  .contact-list svg { width: 18px; height: 18px; margin-right: 16px; fill: var(--purple); }
  .back__offer {
    position: absolute;
    left: 60px;
    top: 387px;
    font-size: 28px;
    color: var(--magenta);
    white-space: nowrap;
  }
  .back__offer strong { font-weight: 700; font-style: italic; }
</style>
</head>
<body>

<section class="card card--front" aria-label="Business card front">
  <div class="card__backdrop" role="img" aria-label="Soft pink bokeh backdrop with floating white hearts"></div>
  <div class="brand-name front__name">Lumora</div>
  <div class="front__tagline">Activewear</div>
</section>

<section class="card card--back" aria-label="Business card back">
  <div class="card__backdrop" role="img" aria-label="Soft pink bokeh backdrop with floating white hearts"></div>
  <div class="back__band" role="img" aria-label="Purple and mauve curved decorative bands along the right edge">
    <svg viewBox="0 0 1048 594" preserveAspectRatio="none" aria-hidden="true">
      <defs>
        <linearGradient id="band-fill" x1="0" y1="0" x2="1" y2="0">
          <stop offset="0" stop-color="#923a96"/>
          <stop offset="0.55" stop-color="#c87ba8"/>
          <stop offset="1" stop-color="#923a96"/>
        </linearGradient>
      </defs>
      <path fill="url(#band-fill)" d="M640,0 Q900,300 675,594 L1048,594 L1048,0 Z"/>
    </svg>
  </div>

  <div class="brand-name back__name-brand">Lumora</div>
  <div class="back__rule"></div>

  <h1 class="back__person">Harriet Welloby</h1>

  <ul class="contact-list">
    <li>
      <svg viewBox="0 0 24 24" aria-hidden="true"><path d="M6.6 10.8a15.1 15.1 0 0 0 6.6 6.6l2.2-2.2c.3-.3.7-.4 1-.2 1.1.4 2.3.6 3.6.6.6 0 1 .4 1 1V20c0 .6-.4 1-1 1A17 17 0 0 1 3 4c0-.6.4-1 1-1h3.5c.6 0 1 .4 1 1 0 1.3.2 2.5.6 3.6.1.3 0 .7-.2 1z"/></svg>
      0417582064
    </li>
    <li>
      <svg viewBox="0 0 24 24" aria-hidden="true"><path d="M2 5h20v14H2z M4 7v.5l8 5 8-5V7l-8 5z" fill-rule="evenodd"/></svg>
      hattieslumora@mailvento.com
    </li>
    <li>
      <svg viewBox="0 0 24 24" aria-hidden="true"><path d="M12 2a10 10 0 1 0 0 20 10 10 0 0 0 0-20zm6.9 6h-3a15 15 0 0 0-1.3-4 8 8 0 0 1 4.3 4zM12 4c.8 1.2 1.5 2.5 1.9 4h-3.8c.4-1.5 1.1-2.8 1.9-4zM4.3 14a8 8 0 0 1 0-4h3.4a16 16 0 0 0 0 4zm.8 2h3a15 15 0 0 0 1.3 4 8 8 0 0 1-4.3-4zm3-8h-3a8 8 0 0 1 4.3-4 15 15 0 0 0-1.3 4zM12 20c-.8-1.2-1.5-2.5-1.9-4h3.8c-.4 1.5-1.1 2.8-1.9 4zm2.3-6H9.7a14 14 0 0 1 0-4h4.6a14 14 0 0 1 0 4zm.3 6a15 15 0 0 0 1.3-4h3a8 8 0 0 1-4.3 4zm1.7-6a16 16 0 0 0 0-4h3.4a8 8 0 0 1 0 4z"/></svg>
      (ABN) 48715290637
    </li>
  </ul>

  <p class="back__offer"><strong>Free</strong> shipping on all orders over <strong>$100</strong></p>
</section>

</body>
</html>
```